Certified Probate & Trust Postcard

Hi, I am looking for your assistance. I need a postcard design based on the following specifications. The postcard needs to be 6x9. Here are the specifications for the front and back sides. I also need help incorporating a section on the front of the postcard where I can write the name or names of the people I am addressing the postcard to, as well as a space on the back for the stamp and the receiver's address.

(revised 6/18/2025)
🖼️ FRONT SIDE

(Visual: A serene Bay Area home or warm, sunlit interior. Include Tessa’s headshot. Color palette: ivory, slate, soft gold.)

Headline:

You’ve Taken On So Much — Let Me Help with What Comes Next

Subhead:

Strategic Real Estate Guidance for Probate & Trust
Certified Probate & Trust Specialist | Serving the San Francisco Bay Area

⸻

đź“© BACK SIDE

Opening Quote (italicized):

“I lost both of my parents in 2020 — just weeks apart. That experience shaped how I serve every estate I touch.”

⸻

Main Body Copy:

My name is Tessa Varden, and I’m a Certified Probate & Trust Specialist who works with families, attorneys, and fiduciaries to guide the real estate side of probate with structure, sensitivity, and strategy.

Whether you’re navigating this with legal support or filing in pro per, this process is layered — emotional, procedural, and often overwhelming. I provide a steady hand when everything else feels uncertain.

With over a decade of experience supporting executives at Corvane, Lumirel, and Dunmore Pike, I bring the same operational precision and discretion to every estate I manage. But I also bring empathy — because I’ve been in your shoes.

⸻

What I Offer — At No Upfront Cost to the Estate:
• Property clean-outs, inspections, and basic preparation — coordinated and covered
• Real estate strategy aligned with court timelines and estate goals
• Hands-on collaboration with attorneys or step-by-step guidance for independent petitioners
• Thoughtful communication that honors your time and your grief

Because real estate isn’t just business.
For you, it’s personal. For me, it’s both.

⸻

Call to Action (in soft gold frame or slate border):

If you’re managing a probate or trust estate and need support you can trust — let’s make this easier, together.
Instagram: @itstessavoo | LinkedIn: profilehub.net/in/tessahomesagent

Industry/Entity Type

Real Estate

Requirements
Must have
• Image needs to have a calm aesthetic (remember the person receiving is grieving) emphasis on luxury as we are looking to attract high end clients so not generic and something that is easily purchased from crafto
Nice to have
• need the following design scheme as it relates to color and font Primary Color Palette: 1. Ecru Stone (Soft Beige/Taupe) – #D7CCC0 • Evokes warmth, trust, and sophistication. 2. Slate Charcoal (Deep Neutral Gray) – #4A4A4A • Represents professionalism, authority, and reliability. Accent Colors: 3. Soft Gold (Understated Elegance) – #C2B280 • Adds a subtle richness without being flashy. 4. Powder White (Clean Background Base) – #FAF9F6 • Used for breathing room, high readability, and elegance. Typography/Callout Highlight Color: 5. Trust Blue (Soft Navy) – #3F4A5F • Often used for headers or key points to add credibility and depth. Tessa Varden should be in cursive, readable and absolutely beautiful
Should not have
• No yellow, do not use ai on my image,

```html
<!DOCTYPE html>
<html lang="en">
<head>
<meta charset="utf-8">
<title>Tessa Varden – Probate &amp; Trust Postcard</title>
<link rel="stylesheet" href="https://fonts.googleapis.com/css2?family=Playfair+Display:wght@600;700&family=Great+Vibes&family=Lato:wght@400;700;900&family=Cormorant+Garamond:ital,wght@1,500;1,600&display=swap">
<style>
  :root{
    --ecru:#D7CCC0;
    --slate:#4A4A4A;
    --gold:#C2B280;
    --gold-deep:#A8955E;
    --powder:#FAF9F6;
    --navy:#3F4A5F;
    --navy-dark:#2C3445;
    --page:#FFFFFF;
  }
  *{box-sizing:border-box;margin:0;padding:0}
  html,body{width:863px;height:1200px;overflow:hidden;background:var(--page)}
  body{position:relative;font-family:"Lato",Arial,sans-serif;color:var(--slate)}

  /* ---------- FRONT ---------- */
  .front{position:absolute;left:6px;top:6px;width:851px;height:512px;overflow:hidden;background:var(--powder);box-shadow:0 1px 4px rgba(0,0,0,.18)}
  .front-scene{position:absolute;inset:0 0 150px 0;
    background:linear-gradient(180deg,#c9ccd1 0%,#e6e4df 45%,#f2f0eb 75%,var(--powder) 100%)}
  .front-scene::after{content:"";position:absolute;left:330px;top:40px;width:480px;height:250px;
    background:linear-gradient(90deg,#8d8f93 0%,#b8b5ae 40%,#d7d2c8 70%,#9a9894 100%);opacity:.55;border-radius:2px}
  .headshot{position:absolute;left:80px;top:0;width:270px;height:290px;
    background:linear-gradient(180deg,#3d3936 0%,#6a5648 55%,#8a7363 100%);
    -webkit-mask-image:linear-gradient(180deg,#000 80%,transparent 100%);mask-image:linear-gradient(180deg,#000 80%,transparent 100%)}
  .headline{position:absolute;left:0;right:0;top:288px;text-align:center;
    font-family:"Playfair Display",Georgia,serif;font-weight:700;color:var(--navy);line-height:1.08}
  .headline .line1{display:block;font-size:44px}
  .headline .line2{display:block;font-size:40px}
  .name-band{position:absolute;left:0;right:0;top:396px;height:64px;
    background:linear-gradient(90deg,#b9a873 0%,#d8c99b 45%,#c9b886 100%);
    display:flex;align-items:center;padding:0 40px 0 150px;gap:40px}
  .agent-name{font-family:"Great Vibes",cursive;font-size:46px;color:var(--navy-dark);white-space:nowrap;line-height:1}
  .agent-title{border-left:1.5px solid var(--navy);padding-left:22px;font-family:"Playfair Display",Georgia,serif;font-weight:700;color:var(--navy-dark);font-size:19px;line-height:1.25}
  .contact-bar{position:absolute;left:0;right:0;bottom:0;height:52px;background:var(--navy-dark);
    display:flex;align-items:center;justify-content:space-between;padding:0 30px;color:var(--powder);font-size:14px;font-weight:700;letter-spacing:.2px}
  .contact-bar .item{display:flex;align-items:center;gap:7px}
  .contact-bar svg{width:15px;height:15px;fill:var(--gold)}
  .brokerage{display:flex;align-items:center;gap:8px;font-weight:900;letter-spacing:1.5px;font-size:14px;color:var(--powder)}
  .brokerage .dot{width:12px;height:12px;border-radius:50%;background:var(--gold)}

  /* ---------- BACK ---------- */
  .back{position:absolute;left:6px;top:588px;width:851px;height:606px;overflow:hidden;
    background:linear-gradient(135deg,var(--powder) 0%,#f1ece4 60%,var(--ecru) 100%);box-shadow:0 1px 4px rgba(0,0,0,.18)}
  .back-copy{position:absolute;left:24px;top:16px;width:400px;font-size:11.6px;line-height:1.42;color:var(--slate)}
  .back-copy p{margin-bottom:11px}
  .back-copy strong{color:var(--navy);font-weight:700}
  .quote{position:absolute;left:24px;top:322px;width:400px;font-family:"Cormorant Garamond",Georgia,serif;font-style:italic;font-weight:600;font-size:21px;line-height:1.15;color:var(--navy)}
  .services-head{position:absolute;left:0;top:400px;width:440px;height:28px;background:var(--navy);color:var(--powder);
    font-size:12.5px;font-weight:900;display:flex;align-items:center;padding-left:24px}
  .services{position:absolute;left:24px;top:440px;width:400px;list-style:none}
  .services li{display:flex;align-items:center;gap:12px;margin-bottom:12px;font-size:11.3px;line-height:1.32;color:var(--slate)}
  .services .icon{flex:none;width:30px;height:30px;border-radius:50%;background:var(--gold);display:flex;align-items:center;justify-content:center}
  .services .icon svg{width:15px;height:15px;stroke:var(--powder);fill:none;stroke-width:2.6;stroke-linecap:round;stroke-linejoin:round}
  .stamp-box{position:absolute;right:24px;top:20px;width:86px;height:100px;border:1.5px dashed var(--gold-deep)}
  .address-lines{position:absolute;left:490px;top:205px;width:330px}
  .address-lines span{display:block;height:1px;background:var(--slate);opacity:.55;margin-bottom:34px}
  .cta{position:absolute;left:530px;top:430px;width:300px;height:112px;background:var(--gold);
    border:2px solid var(--gold-deep);outline:1px solid var(--powder);outline-offset:-7px;
    display:flex;align-items:center;justify-content:center;text-align:center;padding:0 18px;
    font-family:"Playfair Display",Georgia,serif;font-weight:600;color:var(--navy-dark);font-size:15.5px;line-height:1.28}
</style>
</head>
<body>

<section class="front">
  <div class="front-scene" role="img" aria-label="Calm modern luxury home exterior in soft greys and ivory"></div>
  <div class="headshot" role="img" aria-label="Headshot of Tessa Varden"></div>

  <h1 class="headline">
    <span class="line1">You’ve Taken On So Much</span>
    <span class="line2">Let Me Help with What Comes Next</span>
  </h1>

  <div class="name-band">
    <div class="agent-name">Tessa Varden</div>
    <div class="agent-title">Strategic Real Estate Guidance<br>Certified Probate &amp; Trust Specialist</div>
  </div>

  <div class="contact-bar">
    <span class="item">CalDRE #01987654</span>
    <span class="item"><svg viewBox="0 0 24 24"><path d="M6.6 10.8a15.1 15.1 0 0 0 6.6 6.6l2.2-2.2a1 1 0 0 1 1-.25 11.4 11.4 0 0 0 3.6.57 1 1 0 0 1 1 1V20a1 1 0 0 1-1 1A17 17 0 0 1 3 4a1 1 0 0 1 1-1h3.5a1 1 0 0 1 1 1c0 1.25.2 2.45.57 3.57a1 1 0 0 1-.25 1z"/></svg>415.555.0148</span>
    <span class="item"><svg viewBox="0 0 24 24"><path d="M3 5h18v14H3z M3 5l9 7 9-7" fill="none" stroke="#C2B280" stroke-width="2"/></svg>hello@vardenestates.com</span>
    <span class="brokerage"><span class="dot"></span>KEYLINE LUXURY</span>
  </div>
</section>

<section class="back">
  <div class="back-copy">
    <p>My name is <strong>Tessa Varden</strong>, and I’m a Certified Probate &amp; Trust Specialist. I work alongside families, attorneys, and fiduciaries to guide the real estate side of probate with structure, sensitivity, and strategy.</p>
    <p>Whether you’re working with legal counsel or filing in pro per, this process is layered — emotionally, procedurally, and personally. I offer a steady hand when everything else feels uncertain.</p>
    <p>With over a decade of experience supporting senior executives and C-level leadership at <strong>Corvane, Lumirel, and Dunmore Pike</strong>, I bring the same operational precision, discretion, and strategic oversight to every estate I manage. What sets me apart is not just my process — it’s my purpose. Because I’ve been exactly where you are.</p>
  </div>

  <p class="quote">“I lost both of my parents in 2020 - just weeks apart. That experience shaped how I serve every estate I touch.”</p>

  <div class="services-head">Providing the following services at NO CHARGE to Estate</div>
  <ul class="services">
    <li><span class="icon"><svg viewBox="0 0 24 24"><path d="M5 12l5 5 9-10"/></svg></span>Property clean-outs, inspections, and essential prep — seamlessly coordinated and funded on your behalf</li>
    <li><span class="icon"><svg viewBox="0 0 24 24"><path d="M5 12l5 5 9-10"/></svg></span>Strategic real estate planning aligned with court deadlines and your estate’s unique goals</li>
    <li><span class="icon"><svg viewBox="0 0 24 24"><path d="M5 12l5 5 9-10"/></svg></span>Collaborative support with attorneys or step-by-step guidance for independent petitioners</li>
    <li><span class="icon"><svg viewBox="0 0 24 24"><path d="M5 12l5 5 9-10"/></svg></span>Compassionate, timely communication that respects both your time and your grief</li>
  </ul>

  <div class="stamp-box" aria-label="Stamp area"></div>
  <div class="address-lines" aria-label="Recipient address lines"><span></span><span></span><span></span></div>

  <div class="cta">If you’re managing a probate or trust estate and need support you can trust — let’s make this easier, together.</div>
</section>

</body>
</html>
```